Website for a online coaching platform

I would like a website designed with the same content the same as the one below:

https://www.corvel-ashby.com/

New practitioner Marek Tollvander

Target Market(s)

Injured athletes for treatment and medcal professionals for education

Industry/Entity Type

Professional sport and medical education

Coding

Coded - Design and coding required

Number of Pages Required

5+ page

Colors

Designer to choose colors to be used in the design.

Requirements
Must have
• Same amount and format of pages as sample website

```html
<!DOCTYPE html>
<html lang="en">
<head>
<meta charset="utf-8">
<title>KVR Performance – Performance Rehabilitation Specialist</title>
<link rel="stylesheet" href="https://fonts.googleapis.com/css2?family=Montserrat:wght@400;500;600;700;800&display=swap">
<style>
:root{
  --green:#4cae4f;
  --blue:#2b6bc8;
  --orange:#f19a3e;
  --ink:#111111;
  --text:#333333;
  --card:#efefef;
  --footer:#7d8787;
  --white:#ffffff;
}
*{margin:0;padding:0;box-sizing:border-box}
html,body{width:1200px;height:4996px;overflow:hidden}
body{font-family:"Montserrat",sans-serif;color:var(--text);background:var(--white);position:relative}
.abs{position:absolute}
.btn{position:absolute;display:flex;align-items:center;justify-content:center;background:var(--green);color:var(--white);border-radius:30px;font-size:13px;font-weight:600;letter-spacing:.5px;text-transform:uppercase}
.photo{position:absolute;border-radius:16px}

/* hero */
.hero{position:absolute;left:0;top:0;width:1200px;height:651px;background:linear-gradient(120deg,#8a8580 0%,#6d6a68 45%,#4f4a48 100%)}
.hero-shade{position:absolute;inset:0;background:rgba(0,0,0,.28)}
.logo{position:absolute;color:var(--white);font-weight:800;line-height:1}
.logo .mark{font-size:48px;letter-spacing:-1px;display:block}
.logo .sub{font-size:11px;letter-spacing:2px;display:block;margin-top:4px}
.social{position:absolute;width:38px;height:38px;border-radius:50%;display:flex;align-items:center;justify-content:center;font-size:8px;font-weight:600}
.hero .social{border:2px solid var(--white);color:var(--white)}
.nav-line{position:absolute;left:74px;top:101px;width:1050px;height:1px;background:rgba(255,255,255,.7)}
.nav{position:absolute;top:113px;font-size:13px;font-weight:500;color:var(--white);text-transform:uppercase}
.nav.active{color:var(--orange)}
.hero-title{position:absolute;left:0;width:1200px;top:270px;text-align:center;color:var(--white);font-weight:800;font-size:40px;line-height:43px;text-transform:uppercase}
.hero-sub{position:absolute;left:0;width:1200px;top:372px;text-align:center;color:var(--white);font-weight:700;font-size:19px}
.dot{position:absolute;top:601px;width:13px;height:13px;border-radius:50%;background:var(--white)}
.dot.on{background:var(--orange)}

/* about */
.card{position:absolute;background:var(--card);border-radius:16px;padding:30px 24px}
.h2{font-weight:800;color:var(--ink);text-transform:uppercase}
.body{font-size:14.5px;line-height:24.6px;color:var(--text)}

/* workshops */
.workshops{position:absolute;left:0;top:1248px;width:1200px;height:595px;background:var(--blue)}
.ws{position:absolute;top:132px;width:329px}
.ws .img{height:194px;border-radius:12px;position:relative}
.ws .date{position:absolute;right:20px;bottom:14px;width:56px;height:64px;background:var(--green);border-radius:8px;color:var(--white);text-align:center;font-weight:700}
.ws .date span{display:block;font-size:13px;padding-top:6px}
.ws .date b{display:block;font-size:31px;line-height:34px}
.ws h3{color:var(--white);font-size:17px;font-weight:600;line-height:23px;margin-top:20px;text-transform:uppercase}
.ws p{color:#e8eefa;font-size:14px;line-height:20px;margin-top:8px}
.pill{margin-top:22px;width:242px;height:45px;border-radius:25px;background:var(--white);display:flex;overflow:hidden}
.pill .who{flex:1;display:flex;align-items:center;padding-left:12px;font-size:14px;font-weight:700;color:var(--ink)}
.pill .time{width:78px;background:var(--orange);color:var(--white);display:flex;align-items:center;justify-content:center;font-size:14px;border-radius:25px}

/* practitioner */
.practitioner{position:absolute;left:0;top:1843px;width:1200px;height:618px;background:linear-gradient(180deg,#ffffff 40%,#ececec 100%)}

/* testimonials */
.t-name{font-size:24px;font-weight:700;color:var(--ink)}
.t-role{font-size:14.5px;font-weight:700;color:var(--green);margin-top:8px}
.t-card{padding:26px 24px}
.t-card .body{margin-top:10px}

/* clients */
.clients{position:absolute;left:0;top:4099px;width:1200px;height:746px;background:#f7f7f7}
.client{position:absolute;width:140px;text-align:center;font-size:15px;font-weight:700;color:#2d2d2d;line-height:19px;display:flex;flex-direction:column;align-items:center;gap:8px}
.client i{display:block;width:44px;height:44px;border-radius:50%;background:#d6d6d6}

/* footer */
.footer{position:absolute;left:0;top:4845px;width:1200px;height:151px;background:var(--footer)}
.footer .social{border:2px solid var(--white);color:var(--white);background:rgba(255,255,255,.1)}
</style>
</head>
<body>

<!-- Hero -->
<section class="hero">
  <div class="abs" role="img" aria-label="Smiling young man in a blue t-shirt with a red cast on his wrist, sitting at home" style="inset:0;background:linear-gradient(110deg,#9c968f 0%,#77716c 40%,#3f5f8f 60%,#5b5552 100%)"></div>
  <div class="hero-shade"></div>
  <div class="logo" style="left:74px;top:19px"><span class="mark">KVR</span><span class="sub">PERFORMANCE</span></div>
  <div class="social" style="left:683px;top:29px">Kiwo</div>
  <div class="social" style="left:729px;top:29px;background:var(--white);color:#c33">Tafl</div>
  <div class="social" style="left:776px;top:29px">Vumo</div>
  <div class="social" style="left:824px;top:29px">Nexa</div>
  <div class="btn" style="left:882px;top:25px;width:242px;height:47px">Book KVR Performance</div>
  <div class="nav-line"></div>
  <div class="nav active" style="left:105px">Home</div>
  <div class="nav" style="left:194px">About Us</div>
  <div class="nav" style="left:312px">Rehabilitation Specialist</div>
  <div class="nav" style="left:560px">Researcher</div>
  <div class="nav" style="left:703px">Educator</div>
  <div class="nav" style="left:827px">Event Calendar</div>
  <div class="nav" style="left:1002px">Contact Us</div>
  <h1 class="hero-title">Performance<br>Rehabilitation Specialist</h1>
  <p class="hero-sub">Expertise in Rehabilitation, Injury Prevention and Athletic Performance</p>
  <div class="btn" style="left:479px;top:430px;width:242px;height:45px">Book KVR Performance</div>
  <span class="dot" style="left:564px"></span><span class="dot on" style="left:585px"></span><span class="dot" style="left:606px"></span><span class="dot" style="left:628px"></span>
</section>

<!-- About -->
<section class="about">
  <div class="photo" role="img" aria-label="Clinician in a white coat holding a tablet beside a laptop" style="left:74px;top:721px;width:600px;height:442px;background:linear-gradient(135deg,#d9e3e6 0%,#b9c9cf 50%,#eef2f3 100%)"></div>
  <div class="abs" style="left:975px;top:769px;width:165px;height:161px;background:var(--orange);border-radius:14px"></div>
  <div class="abs" style="left:702px;top:1085px;width:162px;height:29px;background:var(--blue);border-radius:0 0 14px 14px"></div>
  <div class="card" style="left:587px;top:783px;width:539px;height:318px">
    <h2 class="h2" style="font-size:31px">About KVR Performance</h2>
    <p class="body" style="margin-top:14px">Sed ut perspiciatis unde omnis iste natus error sit voluptatem accusantium doloremque laudantium, totam rem aperiam, eaque ipsa quae ab illo inventore veritatis et quasi architecto beatae vitae dicta sunt explicabo. Nemo enim ipsam voluptatem quia voluptas sit aspernatur aut odit aut fugit.</p>
  </div>
  <div class="btn" style="left:607px;top:1008px;width:159px;height:48px">Read More</div>
</section>

<!-- Workshops -->
<section class="workshops">
  <h2 class="h2 abs" style="left:74px;top:68px;font-size:33px;color:var(--white)">Training <span style="font-weight:600">Workshops</span></h2>
  <svg class="abs" style="left:1070px;top:72px" width="60" height="24" viewBox="0 0 60 24" fill="none" stroke-width="3" stroke-linecap="round">
    <path d="M16 4 L8 12 L16 20" stroke="var(--orange)"/>
    <path d="M44 4 L52 12 L44 20" stroke="#ffffff"/>
  </svg>
  <article class="ws" style="left:74px">
    <div class="img" role="img" aria-label="Physiotherapy session with a wheelchair athlete stretching in a living room" style="background:linear-gradient(135deg,#8a6f55,#c9b39a 60%,#5e5a57)"><div class="date"><span>Aug</span><b>08</b></div></div>
    <h3>Advanced ACL<br>Rehabilitation Workshop</h3>
    <p>Equip yourself with the necessary tools and knowledge to start your own successful business venture.</p>
    <div class="pill"><span class="who">Marek Tollvander</span><span class="time">08:00</span></div>
  </article>
  <article class="ws" style="left:436px">
    <div class="img" role="img" aria-label="Man sitting on the floor using a tablet" style="background:linear-gradient(135deg,#e8e6e2,#a8b4bf 55%,#3d4a5a)"><div class="date"><span>Aug</span><b>08</b></div></div>
    <h3>Advanced ACL<br>Rehabilitation Workshop</h3>
    <p>Equip yourself with the necessary tools and knowledge to start your own successful business venture.</p>
    <div class="pill"><span class="who">Marek Tollvander</span><span class="time">08:00</span></div>
  </article>
  <article class="ws" style="left:798px">
    <div class="img" role="img" aria-label="Therapist holding a foam roller in a clinic" style="background:linear-gradient(135deg,#f0f2f2,#b8d8d8 55%,#6a5aa0)"><div class="date"><span>Aug</span><b>08</b></div></div>
    <h3>Advanced ACL<br>Rehabilitation Workshop</h3>
    <p>Equip yourself with the necessary tools and knowledge to start your own successful business venture.</p>
    <div class="pill"><span class="who">Marek Tollvander</span><span class="time">08:00</span></div>
  </article>
</section>

<!-- New practitioner -->
<section class="practitioner">
  <h2 class="h2 abs" style="left:74px;top:126px;font-size:31px;line-height:37px">Meet New Practitioner<br>Marek Tollvander</h2>
  <div class="abs" style="left:74px;top:213px;width:600px">
    <p class="body">Sed ut perspiciatis unde omnis iste natus error sit voluptatem accusantium doloremque laudantium, totam rem aperiam, eaque ipsa quae ab illo inventore veritatis et quasi architecto beatae vitae dicta sunt explicabo. Nemo enim ipsam voluptatem quia voluptas sit aspernatur aut odit aut fugit.</p>
    <p class="body" style="margin-top:8px">Nemo enim ipsam voluptatem quia voluptas sit aspernatur aut odit aut fugit, sed quia consequuntur magni dolores eos qui ratione voluptatem sequi nesciunt.</p>
  </div>
  <div class="btn" style="left:74px;top:422px;width:161px;height:49px">Read More</div>
  <div class="photo" role="img" aria-label="Doctor in a white coat with glasses and a stethoscope holding a tablet" style="left:703px;top:72px;width:423px;height:459px;border-radius:22px;background:linear-gradient(135deg,#e4e7ea,#cfd5da 50%,#f2f3f4)"></div>
</section>

<!-- Testimonials -->
<section class="testimonials">
  <h2 class="h2 abs" style="left:0;width:1220px;top:2521px;text-align:center;font-size:33px">Our Testimonials</h2>

  <div class="photo" role="img" aria-label="Smiling man sitting on an exercise mat with a water bottle and phone" style="left:74px;top:2628px;width:600px;height:442px;background:linear-gradient(135deg,#e6e6e2,#c7c3bb 50%,#8a90a6)"></div>
  <div class="card t-card" style="left:587px;top:2692px;width:539px;height:316px">
    <h3 class="t-name">Name Heading</h3>
    <p class="t-role">Neque porro quisquam est, qui dolorem ipsum quia</p>
    <p class="body">“ Sed ut perspiciatis unde omnis iste natus error sit voluptatem accusantium doloremque laudantium, totam rem aperiam, eaque ipsa quae ab illo inventore veritatis et quasi architecto beatae vitae dicta sunt explicabo. Nemo enim ipsam voluptatem quia voluptas sit aspernatur aut odit aut fugit enim ad minima veniam, quis nostrum exercitationem ullam corporis suscipit la boriosam, nisi ut aliquid..”</p>
  </div>

  <div class="photo" role="img" aria-label="Smiling woman in sportswear looking at her phone in a gym" style="left:525px;top:3103px;width:601px;height:440px;background:linear-gradient(135deg,#4a4f52,#2e3234 50%,#6b6158)"></div>
  <div class="card t-card" style="left:74px;top:3167px;width:540px;height:314px">
    <h3 class="t-name">Name Heading</h3>
    <p class="t-role">Neque porro quisquam est, qui dolorem ipsum quia</p>
    <p class="body">“ Sed ut perspiciatis unde omnis iste natus error sit voluptatem accusantium doloremque laudantium, totam rem aperiam, eaque ipsa quae ab illo inventore veritatis et quasi architecto beatae vitae dicta sunt explicabo. Nemo enim ipsam voluptatem quia voluptas sit aspernatur aut odit aut fugit enim ad minima veniam, quis nostrum exercitationem ullam corporis suscipit la boriosam, nisi ut aliquid..”</p>
  </div>

  <div class="photo" role="img" aria-label="Woman with glasses sitting cross-legged holding a tablet in a fitness studio" style="left:74px;top:3572px;width:600px;height:440px;background:linear-gradient(135deg,#d8dcd3,#a9c98a 55%,#e9ece6)"></div>
  <div class="card t-card" style="left:587px;top:3636px;width:539px;height:314px">
    <h3 class="t-name">Name Heading</h3>
    <p class="t-role">Neque porro quisquam est, qui dolorem ipsum quia</p>
    <p class="body">“ Sed ut perspiciatis unde omnis iste natus error sit voluptatem accusantium doloremque laudantium, totam rem aperiam, eaque ipsa quae ab illo inventore veritatis et quasi architecto beatae vitae dicta sunt explicabo. Nemo enim ipsam voluptatem quia voluptas sit aspernatur aut odit aut fugit enim ad minima veniam, quis nostrum exercitationem ullam corporis suscipit la boriosam, nisi ut aliquid..”</p>
  </div>
</section>

<!-- Past clients -->
<section class="clients">
  <h2 class="h2 abs" style="left:0;width:1220px;top:60px;text-align:center;font-size:33px">Past Clients</h2>
  <div class="client" style="left:70px;top:160px"><i></i>Southern Roos</div>
  <div class="client" style="left:244px;top:160px"><i></i>Redrose Union</div>
  <div class="client" style="left:389px;top:160px"><i></i>Four Nations XV</div>
  <div class="client" style="left:523px;top:160px"><i></i>Valley Union</div>
  <div class="client" style="left:674px;top:160px"><i></i>Riverside Reds</div>
  <div class="client" style="left:823px;top:160px"><i></i>Northgate FC</div>
  <div class="client" style="left:978px;top:160px"><i></i>Tyneward FC</div>

  <div class="client" style="left:70px;top:312px"><i></i>Seahawks RFC</div>
  <div class="client" style="left:244px;top:312px"><i></i>Stade Ouest</div>
  <div class="client" style="left:389px;top:312px"><i></i>Emerald Union</div>
  <div class="client" style="left:674px;top:312px"><i></i>Aire Valley FC</div>
  <div class="client" style="left:823px;top:312px"><i></i>Kirkby Town</div>
  <div class="client" style="left:978px;top:312px"><i></i>Eastfield City</div>

  <div class="client" style="left:70px;top:458px"><i></i>Midland Cats</div>
  <div class="client" style="left:221px;top:458px"><i></i>Spa City RFC</div>
  <div class="client" style="left:453px;top:458px"><i></i>Bayside AFC</div>
  <div class="client" style="left:674px;top:458px"><i></i>Colne Valley</div>
  <div class="client" style="left:823px;top:458px"><i></i>Seafront FC</div>
  <div class="client" style="left:984px;top:458px"><i></i>Cliffside AFC</div>

  <div class="btn" style="left:504px;top:628px;width:192px;height:48px">Load More Clients</div>
</section>

<!-- Footer -->
<footer class="footer">
  <div class="logo" style="left:74px;top:39px"><span class="mark">KVR</span><span class="sub">PERFORMANCE</span></div>
  <p class="abs" style="left:0;width:1200px;top:70px;text-align:center;color:var(--white);font-size:13px">Copyright © 2025 Company Name All rights reserved</p>
  <div class="social" style="left:946px;top:58px">Kiwo</div>
  <div class="social" style="left:993px;top:58px;background:var(--white);color:var(--blue)">Tafl</div>
  <div class="social" style="left:1039px;top:58px">Vumo</div>
  <div class="social" style="left:1088px;top:58px">Nexa</div>
</footer>

</body>
</html>
```